Business Card Design Project

I have a two letter domain name vu.com.au (lower case font please). I want a business card, cum logo that is die cut (around the vu segment at least) that fits standard business card size.
vu is all about what 'I am' - a journalist, blogger, analyst, commentator. My mantra is "I think therefore vu'.
The reverse of the card only needs my name Ned Pike, email ned@vu.com.au and mobile +61 400 555 123
Target Market(s)
Mainly people that will use my professional writing services and suppliers that will provide product for review
Industry/Entity Type
Business
Requirements
Must have
- One side is vu.com.au (hint - the .com.au can be vertical or horizontal to fit - the vu should be as large as possible).
The other requires large size font name, email and phone details (so no one needs glasses to read it).
The die cut can be just to highlight the vu segment - need not be around the whole card.
Font used in the past was Belwe (old style - very much like the i used in the information symbol).
Colours - no preference - prefer two colour to process colour but can also be an outline font instead of solid colour.

```html
<!DOCTYPE html>
<html lang="en">
<head>
<meta charset="utf-8">
<title>vu.com.au — Business Card</title>
<link rel="stylesheet" href="https://fonts.googleapis.com/css2?family=Comfortaa:wght@700&family=Orbitron:wght@700&family=Poiret+One&display=swap">
<style>
  :root {
    --page: #ffffff;
    --card: #000000;
    --ink: #ffffff;
    --accent: #f0501e;
  }
  * { margin: 0; padding: 0; box-sizing: border-box; }
  html, body {
    width: 1200px;
    height: 900px;
    overflow: hidden;
    background: var(--page);
  }
  .sheet {
    position: relative;
    width: 1200px;
    height: 900px;
  }
  .card {
    position: absolute;
    left: 347px;
    width: 557px;
    height: 363px;
    background: var(--card);
    overflow: hidden;
  }
  .card--front { top: 60px; }
  .card--back  { top: 473px; }
  .card-art {
    position: absolute;
    inset: 0;
    width: 557px;
    height: 363px;
  }
  .card-art .brand-name,
  .card-art .domain {
    fill: var(--ink);
    font-family: "Comfortaa", sans-serif;
    font-weight: 700;
  }
  .card-art .brand-name { font-size: 240px; }
  .card-art .domain { font-size: 34px; }
  .holder-name {
    position: absolute;
    left: 38px;
    top: 33px;
    font-family: "Poiret One", sans-serif;
    font-weight: 400;
    font-size: 29px;
    line-height: 1;
    letter-spacing: 1px;
    color: var(--accent);
    text-transform: uppercase;
  }
  .divider {
    position: absolute;
    left: 195px;
    top: 17px;
    width: 1.5px;
    height: 70px;
    background: var(--ink);
  }
  .contact {
    position: absolute;
    left: 204px;
    top: 33px;
    font-family: "Orbitron", sans-serif;
    font-weight: 700;
    font-size: 15px;
    line-height: 15px;
    color: var(--ink);
    text-transform: uppercase;
    font-style: normal;
    white-space: nowrap;
  }
  .contact-phone { display: block; padding-left: 6px; }
  .contact-email { display: block; }
</style>
</head>
<body>
<main class="sheet">

  <section class="card card--front" aria-label="Card front">
    <svg class="card-art" viewBox="0 0 557 363">
      <text class="brand-name" x="170" y="335">vu</text>
      <text class="domain" x="556" y="212" transform="rotate(-90 556 212)">.com.au</text>
    </svg>
  </section>

  <section class="card card--back" aria-label="Card back">
    <svg class="card-art" viewBox="0 0 557 363">
      <text class="brand-name" x="120" y="335">vu</text>
      <text class="domain" x="1" y="64" transform="rotate(90 1 64)">.com.au</text>
    </svg>
    <h1 class="holder-name">Ned Pike</h1>
    <span class="divider"></span>
    <address class="contact">
      <span class="contact-phone">+61 400 555 123</span>
      <span class="contact-email">ned@vu.com.au</span>
    </address>
  </section>

</main>
</body>
</html>
```